FotoVELTA buisnesscard

Hey :) I need a modern buisnesscard for my company FotoVELTA
It most have:
Dagligleder og Fotograf: Henrik Torvald Bjelland

Mob: +4791642058
Epost: post@fotovelta.no
Adresse: Bakkestien22, 5148 Nordvika

Facbook and instagram logo with text FotoVELTA

FotoVELTA logo

It Company

```html
<!DOCTYPE html>
<html lang="no">
<head>
<meta charset="utf-8">
<title>FotoVELTA – visittkort</title>
<link href="https://fonts.googleapis.com/css2?family=Exo+2:wght@600;700&family=Roboto:wght@400;500&display=swap" rel="stylesheet">
<style>
  :root {
    --backdrop: #3a302c;
    --card: #141414;
    --card-edge: #1f1f1f;
    --white: #ffffff;
    --silver: #cfcfcf;
    --accent: #e02424;
    --divider: #5a5a5a;
    --muted: #e6e6e6;
  }
  * { margin: 0; padding: 0; box-sizing: border-box; }
  html, body {
    width: 1200px;
    height: 900px;
    overflow: hidden;
    background: var(--backdrop);
  }
  .canvas {
    position: relative;
    width: 1200px;
    height: 900px;
    display: flex;
    align-items: center;
    justify-content: center;
    gap: 40px;
  }
  .card {
    position: relative;
    width: 540px;
    height: 310px;
    background: var(--card);
    border: 1px solid var(--card-edge);
    border-radius: 4px;
    box-shadow: 0 14px 30px rgba(0,0,0,0.45);
  }

  /* Contact side */
  .card-contact .wordmark {
    position: absolute;
    left: 44px;
    top: 130px;
    font-family: "Exo 2", sans-serif;
    font-weight: 700;
    font-size: 36px;
    color: var(--white);
    display: flex;
    align-items: center;
    gap: 10px;
  }
  .card-contact .wordmark-square {
    width: 16px;
    height: 16px;
    background: var(--white);
  }
  .card-contact .divider {
    position: absolute;
    left: 268px;
    top: 104px;
    width: 1px;
    height: 96px;
    background: var(--divider);
  }
  .details {
    position: absolute;
    left: 292px;
    top: 92px;
    font-family: "Roboto", sans-serif;
  }
  .details .name {
    font-family: "Exo 2", sans-serif;
    font-weight: 700;
    font-size: 17px;
    color: var(--white);
    letter-spacing: 0.2px;
  }
  .details .role {
    font-size: 12px;
    color: var(--accent);
    margin: 3px 0 9px;
  }
  .contact-list { list-style: none; }
  .contact-list li {
    display: flex;
    align-items: center;
    gap: 8px;
    font-size: 12.5px;
    color: var(--muted);
    line-height: 18px;
  }
  .contact-list svg { width: 10px; height: 10px; flex: none; }
  .social {
    position: absolute;
    right: 44px;
    bottom: 60px;
    display: flex;
    align-items: center;
    gap: 8px;
    font-family: "Roboto", sans-serif;
    font-size: 13px;
    color: var(--muted);
  }
  .social-square {
    width: 12px;
    height: 12px;
    background: var(--accent);
  }

  /* Brand side */
  .card-brand {
    display: flex;
    align-items: center;
    justify-content: center;
  }
  .card-brand .wordmark {
    font-family: "Exo 2", sans-serif;
    font-weight: 700;
    font-size: 52px;
    color: var(--silver);
    display: flex;
    align-items: center;
    gap: 14px;
  }
  .card-brand .wordmark-square {
    width: 22px;
    height: 22px;
    background: var(--silver);
  }
</style>
</head>
<body>
<main class="canvas">
  <section class="card card-contact" aria-label="Kontaktside">
    <div class="wordmark"><span class="wordmark-square"></span>FotoVELTA</div>
    <div class="divider"></div>
    <div class="details">
      <p class="name">Henrik Torvald Bjelland</p>
      <p class="role">Dagligleder og Fotograf</p>
      <ul class="contact-list">
        <li>
          <svg viewBox="0 0 10 10" aria-hidden="true"><rect x="2" y="0.5" width="6" height="9" rx="1" fill="var(--accent)"/><rect x="3" y="1.5" width="4" height="6" fill="var(--card)"/></svg>
          +4791642058
        </li>
        <li>
          <svg viewBox="0 0 10 10" aria-hidden="true"><rect x="0.5" y="2" width="9" height="6" rx="0.8" fill="var(--accent)"/><path d="M0.8 2.4 L5 5.6 L9.2 2.4" stroke="var(--card)" stroke-width="0.9" fill="none"/></svg>
          post@fotovelta.no
        </li>
        <li>
          <svg viewBox="0 0 10 10" aria-hidden="true"><path d="M5 0.5 C2.6 0.5 1.5 2.2 1.5 3.8 C1.5 6 5 9.5 5 9.5 C5 9.5 8.5 6 8.5 3.8 C8.5 2.2 7.4 0.5 5 0.5 Z" fill="var(--accent)"/><circle cx="5" cy="3.8" r="1.3" fill="var(--card)"/></svg>
          Bakkestien22, 5148 Nordvika
        </li>
      </ul>
    </div>
    <div class="social"><span class="social-square"></span>FotoVELTA</div>
  </section>

  <section class="card card-brand" aria-label="Logoside">
    <div class="wordmark"><span class="wordmark-square"></span>FotoVELTA</div>
  </section>
</main>
</body>
</html>
```